business card for new biz

A business card that looks professional, but is also attractive and just slightly more than conservative. I would like to see either a white background with the type in gray and a shade of blue used as an accent color. The design can be very similar, if not exactly like the card design that I submitted, with a change in information (company name and contact information).
The heading will read: HALVERD & CO. (using an ampersand). the sub-heading to read: Caring business coaching and marketing consulting
Card should also have address of PO Box 4827 Freeland, WA 98163.
Phone should be 206 555 - 0147 and email of halverd@halverdco.example.
I do not have nor do I need a logo. The font used and the ampersand will serve as my logo. Please use a san-serif or a font close to that, that is classy and not too heavy. I like the font used in VORIND, per the card design attached.

Target Market(s)

local businesses that need help with business coaching and marketing consulting

Industry/Entity Type

Marketing

Contact Information for Business Card

A clean, professional looking card.

Font styles to use
Sans Serif

Colors
85acd3
0792cd
3277b5

Requirements
Must have
• a font similar to Michelangelo (an elegant sans serif font) for company name and sub-title. .
• using an attractive and distinctive ampersand.
• Background colors gray or white with accent color of blue
• All information on front. The primary color used for card should be the entire back. Back would have no type, just the solid color.
Nice to have
• A good usage of blue as an accent color to enhance an otherwise conservative business card.
Should not have
• any other colors aside from gray, blue and white

```html
<!DOCTYPE html>
<html lang="en">
<head>
<meta charset="utf-8">
<title>Halverd &amp; Co. Business Card</title>
<link rel="stylesheet" href="https://fonts.googleapis.com/css2?family=Montserrat:wght@600&family=Questrial&display=swap">
<style>
  :root {
    --canvas: #ffffff;
    --card-gray: #c9c9c9;
    --card-edge: #b3b3b3;
    --brand-blue: #1f74b9;
    --pale-blue: #85acd3;
    --ink: #222222;
    --white: #ffffff;
  }
  html, body {
    margin: 0;
    padding: 0;
    width: 1200px;
    height: 548px;
    overflow: hidden;
    background: var(--canvas);
  }
  .card {
    position: absolute;
    top: 96px;
    width: 564px;
    height: 422px;
    overflow: hidden;
    box-sizing: border-box;
  }
  .card-front {
    left: 36px;
    background: var(--card-gray);
    border: 1px solid var(--card-edge);
  }
  .card-back {
    left: 610px;
    width: 566px;
    background: var(--brand-blue);
  }
  .accent-circle {
    position: absolute;
    left: -24px;
    top: -72px;
    width: 410px;
    height: 410px;
    border-radius: 50%;
    background: var(--brand-blue);
  }
  .footer-band {
    position: absolute;
    left: 0;
    right: 0;
    bottom: 0;
    height: 19px;
    background: var(--brand-blue);
  }
  .company-name {
    position: absolute;
    left: 34px;
    top: 100px;
    margin: 0;
    font-family: "Montserrat", sans-serif;
    font-weight: 600;
    font-size: 38px;
    letter-spacing: 0.5px;
    color: var(--white);
    white-space: nowrap;
  }
  .tagline {
    position: absolute;
    left: 34px;
    top: 154px;
    width: 320px;
    margin: 0;
    font-family: "Questrial", sans-serif;
    font-size: 19px;
    line-height: 24px;
    text-align: center;
    color: var(--pale-blue);
  }
  .contact {
    position: absolute;
    right: 30px;
    top: 296px;
    margin: 0;
    font-family: "Questrial", sans-serif;
    font-style: normal;
    font-size: 21px;
    line-height: 24.5px;
    text-align: right;
    color: var(--ink);
    white-space: nowrap;
  }
</style>
</head>
<body>
  <section class="card card-front" aria-label="Card front">
    <div class="accent-circle"></div>
    <h1 class="company-name">HALVERD &amp; CO.</h1>
    <p class="tagline">Caring business coaching<br>and marketing consulting</p>
    <address class="contact">
      Address: PO Box 4827<br>
      Freeland, WA 98163<br>
      Ph # 206 555 - 0147<br>
      Email: halverd@halverdco.example
    </address>
    <div class="footer-band"></div>
  </section>
  <section class="card card-back" aria-label="Card back"></section>
</body>
</html>
```